Premium Olive Oil Bottle Label

Need a double bottle label for our premium olive oil (front and back). Please refer to the brief attached. The label needs to incorporate the elements from the logo designs that we provide in attachment into a single design language. The front panel should capture attention and the back panel provide a story of our unique product.

Target Market(s)

US and Europe

Industry/Entity Type

Food Production

Font styles to use
Other font styles liked:
• Please refer to the Brief

Colors

Designer to choose colors to be used in the design.

Requirements
Must have
• Integrate the elements in the brief into a single premium execution.
Nice to have
• Feel free to use the provided visual elements as a base for your further creative exploration.
Should not have
• Too many colors. Please propose a restricted color palette as the bottle is black matte. The design needs to deliver premium appeal and be distinctive.

```html
<!DOCTYPE html>
<html lang="en">
<head>
<meta charset="utf-8">
<title>Le Haut Vallon – Olive Oil Labels</title>
<link rel="stylesheet" href="https://fonts.googleapis.com/css2?family=Cinzel:wght@400;500&family=Arimo:wght@400;700&display=swap">
<style>
  :root {
    --page: #ffffff;
    --label: #242424;
    --gold: #e6b923;
    --gold-rule: #d9ae1f;
    --antique: #a88f5c;
    --antique-dark: #5e5237;
    --parchment: #cdbf95;
    --ink: #2a2618;
    --white: #ffffff;
  }
  * { margin: 0; padding: 0; box-sizing: border-box; }
  html, body {
    width: 1200px; height: 1200px; overflow: hidden;
    background: var(--page);
  }
  .canvas { position: relative; width: 1200px; height: 1200px; }

  /* Front label */
  .front {
    position: absolute; left: 180px; top: 268px;
    width: 445px; height: 670px;
    background: var(--label);
    color: var(--gold);
    font-family: "Arimo", Arial, sans-serif;
  }
  .crest {
    position: absolute; left: 56px; top: 20px;
    width: 334px; height: 288px;
  }
  .crest-ornament {
    position: absolute; inset: 0;
    border-radius: 40%;
    background: radial-gradient(ellipse at center, rgba(168,143,92,0.05) 30%, rgba(168,143,92,0.28) 62%, rgba(168,143,92,0.06) 80%, transparent 82%);
  }
  .brand {
    position: absolute; left: 0; right: 0; top: 74px;
    text-align: center;
    font-family: "Cinzel", "Times New Roman", serif;
    font-weight: 500;
    color: var(--antique);
    line-height: 1;
  }
  .brand span { display: block; }
  .brand .small { font-size: 44px; margin-bottom: 6px; }
  .brand .large { font-size: 50px; margin-bottom: 6px; }

  .rule {
    position: absolute; left: 68px; width: 308px; height: 2px;
    background: var(--gold-rule);
  }
  .rule.top { top: 318px; }
  .rule.bottom { top: 434px; }

  .product-name {
    position: absolute; left: 0; right: 0; top: 330px;
    text-align: center;
    font-family: "Cinzel", "Times New Roman", serif;
    font-size: 42px; line-height: 48px;
    color: var(--gold);
    letter-spacing: 0.5px;
  }
  .features {
    position: absolute; left: 0; right: 0; top: 448px;
    text-align: center;
    font-size: 17.5px; line-height: 25px;
  }
  .limited {
    position: absolute; left: 0; right: 0; top: 527px;
    text-align: center;
    font-weight: 700; font-size: 21px;
    color: var(--white);
    letter-spacing: 0.3px;
  }
  .origin-banner {
    position: absolute; left: 108px; top: 562px;
    width: 234px; height: 58px;
  }
  .origin-banner svg { position: absolute; inset: 0; }
  .origin-banner p {
    position: absolute; left: 0; right: 0; top: 14px;
    text-align: center;
    font-family: "Cinzel", "Times New Roman", serif;
    font-size: 22px; color: var(--ink);
  }
  .volume, .bottle-no {
    position: absolute; top: 632px;
    font-size: 17.5px;
  }
  .volume { left: 40px; }
  .bottle-no { right: 103px; }

  /* Back label */
  .back {
    position: absolute; left: 674px; top: 124px;
    width: 319px; height: 954px;
    background: var(--label);
    font-family: "Arimo", Arial, sans-serif;
    color: var(--gold);
  }
  .back-frame {
    position: absolute; left: 20px; top: 18px; right: 14px; bottom: 16px;
    border: 3px solid var(--gold-rule);
  }
  .flourish {
    position: absolute; left: 134px; top: 36px;
    width: 56px; height: 16px;
    border-radius: 8px;
    background: linear-gradient(90deg, transparent, rgba(230,185,35,0.7), transparent);
  }
  .story {
    position: absolute; left: 0; right: 0; top: 56px;
    text-align: center;
    font-size: 17.5px; line-height: 27px;
  }
  .story .email { color: var(--white); }
  .mini-crest {
    position: absolute; left: 113px; top: 844px;
    width: 92px; height: 76px;
  }
  .mini-crest .crest-ornament { border-radius: 45%; }
  .mini-crest .brand { top: 14px; color: var(--antique); }
  .mini-crest .brand .small { font-size: 13px; margin-bottom: 1px; }
  .mini-crest .brand .large { font-size: 15px; margin-bottom: 1px; }
</style>
</head>
<body>
<main class="canvas">

  <section class="front" aria-label="Front label">
    <div class="crest">
      <div class="crest-ornament" role="img" aria-label="Ornamental wreath of olive branches, bottle and flourishes framing the estate name"></div>
      <h1 class="brand">
        <span class="small">LE</span>
        <span class="large">HAUT</span>
        <span class="small">VALLON</span>
      </h1>
    </div>

    <div class="rule top"></div>
    <h2 class="product-name">Huile d’Olive<br>Vierge Extra</h2>
    <div class="rule bottom"></div>

    <p class="features">
      From Provence I Organic I Hand-picked<br>
      Artisanal I Single cold-press I Unfiltered<br>
      Late harvest I November 2018
    </p>
    <p class="limited">LIMITED PRODUCTION</p>

    <div class="origin-banner">
      <svg width="234" height="58" viewBox="0 0 234 58" aria-hidden="true">
        <rect x="10" y="8" width="214" height="44" fill="var(--parchment)"/>
        <rect x="2" y="2" width="10" height="54" rx="4" fill="var(--parchment)"/>
        <rect x="222" y="2" width="10" height="54" rx="4" fill="var(--parchment)"/>
      </svg>
      <p>Made in France</p>
    </div>

    <p class="volume">Vol. 500ml</p>
    <p class="bottle-no">Bottle No:</p>
  </section>

  <section class="back" aria-label="Back label">
    <div class="back-frame"></div>
    <div class="flourish" role="img" aria-label="Small gold ornamental flourish"></div>
    <p class="story">
      Nested in the hills of<br>
      Provence, Le Haut Vallon is<br>
      a wild and magical place<br>
      where forest opens up to<br>
      vineyards and olive groves.<br>
      We fell in love with it, and<br>
      you would too! It’s in these<br>
      hills that Aglandau olives<br>
      were grown since Roman<br>
      times, and we were happy to<br>
      bring them back. Our<br>
      production is entirely<br>
      organic, we pick our olives<br>
      by hand and only at the<br>
      point of maturity. We don’t<br>
      harvest our Aglandaus until<br>
      very late in the autumn, and<br>
      use a single mechanical<br>
      cold-press extraction. The<br>
      reward? A very special extra<br>
      virgin oil with its full-on bold<br>
      taste, hints of artichokes and<br>
      fresh-cut grass, and<br>
      remarkably low acidity. Best<br>
      enjoyed before August 2020.<br>
      Do let us know how you<br>
      liked it at<br>
      <span class="email">info@lehautvallon.com!</span><br>
      A+J
    </p>
    <div class="mini-crest">
      <div class="crest-ornament" role="img" aria-label="Small ornamental wreath around the estate name"></div>
      <p class="brand">
        <span class="small">LE</span>
        <span class="large">HAUT</span>
        <span class="small">VALLON</span>
      </p>
    </div>
  </section>

</main>
</body>
</html>
```